Brightwave HR - DL Postcard Fliers

I have a need to get some quotes to create a series of postcard fliers to promote my Human Resources Consultancy & Contracting services. I'd like to start with one to get a feel for how they might look when I introduce other products/services connected to my business. I think DL size would work best (99 x 210 mm). I have enclosed an A4 sheet that has a LOT of content. Would like it to be more visual and less wordy. Id like to feature my broader HR services on back side and the specific product/service offering on the front. For the first one, I would like the focus to be on recruitment. Perhaps need to highlight 20% off as an introductory rate off already cost effective flat rate structure for recruitment. Please keep punchy, less wordy. Happy to review some options you may done for someone else in the past and work with you on final content. Good luck.
Updates

Hi All. I am about 5 days away from making a decision now. I posted a request for an updated logo design last week and am waiting on submissions. Once i have decided on logo design, I will ask you to incorporate into your designs. It will have same coloring and not be too different so should be able to quickly incorporate into your designs. Thanks for your patience.

Target Market(s)

Small to medium enterprises

Industry/Entity Type

Quotes

Font styles to use
Serif

Colors
ec1f27

Requirements
Must have
• Contact Details - mobile, website, email
• Specifics on what product offering is and benefits
• A Call to action
• Ideally double sided DL - landscape view - one side with general information about the business generally, the other side with a specific focus on one product/service offering from within my business.
Should not have
• Too many words.

```html
<!DOCTYPE html>
<html lang="en">
<head>
<meta charset="utf-8">
<title>Brightwave HR – DL Fliers</title>
<link rel="stylesheet" href="https://fonts.googleapis.com/css2?family=Arimo:wght@400;700&family=Roboto+Condensed:wght@400;700&family=Russo+One&display=swap">
<style>
  :root {
    --brand-red: #ec1f27;
    --navy: #13223d;
    --white: #ffffff;
    --backdrop: #1f1f21;
    --photo-dark: #2b2d31;
    --photo-mid: #5d6168;
    --dial-dark: #0a1422;
    --dial-mid: #1f3a5c;
  }
  * { box-sizing: border-box; margin: 0; padding: 0; }
  html, body { width: 1200px; height: 871px; overflow: hidden; background: var(--backdrop); }
  .stage {
    position: relative; width: 1102px; height: 800px;
    transform: scale(1.0889); transform-origin: 0 0;
  }
  .side-label {
    position: absolute; color: var(--white);
    font: 700 17px/1 "Arimo", sans-serif; letter-spacing: 1px;
    transform: rotate(-90deg); transform-origin: left top;
  }
  .side-label--front { left: 27px; top: 178px; }
  .side-label--back { left: 621px; top: 178px; }

  .flyer {
    position: absolute; top: 22px; width: 360px; height: 756px;
    background: var(--white); overflow: hidden;
  }
  .flyer--front { left: 95px; }
  .flyer--back { left: 662px; }
  .flyer__shapes { position: absolute; inset: 0; width: 100%; height: 100%; }

  .brand {
    position: absolute; left: 0; right: 0; top: 252px; height: 62px;
    display: flex; align-items: center; justify-content: center; gap: 12px;
  }
  .brand__mark { width: 22px; height: 22px; background: var(--brand-red); }
  .brand__name { font: 700 34px/1 "Arimo", sans-serif; color: var(--brand-red); }

  .headline {
    position: absolute; left: 0; right: 0; top: 324px; text-align: center;
    font: 700 14.5px/17.5px "Arimo", sans-serif; color: var(--navy); text-transform: uppercase;
  }
  .intro {
    position: absolute; left: 0; right: 0; top: 406px; text-align: center;
    font: 400 13.5px/17.5px "Roboto Condensed", sans-serif; color: var(--white);
  }
  .contact-title {
    position: absolute; left: 0; right: 0; top: 504px; text-align: center;
    font: 700 33px/1 "Arimo", sans-serif; color: var(--brand-red); letter-spacing: .5px;
  }
  .contact-list {
    position: absolute; left: 0; right: 0; top: 547px; text-align: center; list-style: none;
    font: 700 18px/26.5px "Roboto Condensed", sans-serif; color: var(--navy);
  }
  .website {
    position: absolute; left: 0; right: 0; top: 697px; text-align: center;
    font: 700 25px/1 "Roboto Condensed", sans-serif; color: var(--white);
  }

  .offer-title {
    position: absolute; left: 0; right: 0; top: 320px; text-align: center;
    font: 400 21px/1 "Russo One", sans-serif; color: var(--brand-red); text-transform: uppercase;
  }
  .offer-tagline {
    position: absolute; left: 0; right: 0; top: 350px; text-align: center;
    font: 700 12.5px/16px "Arimo", sans-serif; color: var(--navy); text-transform: uppercase;
  }
  .service-list {
    position: absolute; left: 18px; right: 10px; top: 508px; list-style: none;
    font: 400 11px/13.7px "Roboto Condensed", sans-serif; color: var(--navy);
  }
  .service-list li { padding-left: 8px; position: relative; }
  .service-list li::before { content: "•"; position: absolute; left: 0; }
</style>
</head>
<body>
<main class="stage">
  <span class="side-label side-label--front">FRONT</span>
  <span class="side-label side-label--back">BACK</span>

  <!-- Front of flier -->
  <section class="flyer flyer--front">
    <svg class="flyer__shapes" viewBox="0 0 360 756" preserveAspectRatio="none" aria-hidden="true">
      <defs>
        <linearGradient id="frontPhoto" x1="0" y1="0" x2="0" y2="1">
          <stop offset="0" stop-color="var(--photo-dark)"/>
          <stop offset=".6" stop-color="var(--photo-mid)"/>
          <stop offset="1" stop-color="#8b8176"/>
        </linearGradient>
      </defs>
      <path d="M0 0H360V200C250 235 110 230 0 185Z" fill="var(--brand-red)"/>
      <path d="M0 190C110 235 250 238 360 240V245H0Z" fill="var(--white)"/>
      <path d="M0 372C120 400 250 395 360 378V498C250 482 110 478 0 496Z" fill="var(--navy)"/>
      <path d="M0 668C120 652 250 660 360 676V756H0Z" fill="var(--brand-red)"/>
    </svg>
    <div role="img" aria-label="Photo of a businessman holding a network of connected people figures in open hands"
         style="position:absolute;left:0;top:0;width:360px;height:196px;background:linear-gradient(180deg,var(--photo-dark),var(--photo-mid) 65%,#8b8176);clip-path:ellipse(120% 100% at 40% 0%);"></div>

    <div class="brand"><span class="brand__mark"></span><span class="brand__name">Brightwave HR</span></div>
    <h1 class="headline">Your staff...<br>can’t live with them,<br>can’t live without&nbsp; them!</h1>
    <p class="intro">Let us help you ‘brighten’<br>your business by assisting in your HR areas of need,<br>take some of the pain away so you can get o<br>n with the job of growing your business.</p>
    <h2 class="contact-title">CONTACT US</h2>
    <ul class="contact-list">
      <li>Sam Carter</li>
      <li>Director - Brightwave HR</li>
      <li>m: 0400 512 086</li>
      <li>e: scarter@brightwavehr.com.au</li>
    </ul>
    <p class="website">www.brightwavehr.com.au</p>
  </section>

  <!-- Back of flier -->
  <section class="flyer flyer--back">
    <svg class="flyer__shapes" viewBox="0 0 360 756" preserveAspectRatio="none" aria-hidden="true">
      <path d="M0 0H360V200C250 235 110 230 0 185Z" fill="var(--brand-red)"/>
      <path d="M0 190C110 235 250 238 360 240V245H0Z" fill="var(--white)"/>
      <path d="M0 372C120 400 250 395 360 378V498C250 482 110 478 0 496Z" fill="var(--navy)"/>
      <path d="M0 720C120 708 250 712 360 726V756H0Z" fill="var(--brand-red)"/>
    </svg>
    <div role="img" aria-label="Close-up photo of a glowing speedometer dial with a red needle"
         style="position:absolute;left:0;top:0;width:360px;height:196px;background:radial-gradient(circle at 55% 20%,var(--dial-mid),var(--dial-dark) 70%);clip-path:ellipse(120% 100% at 40% 0%);"></div>

    <div class="brand"><span class="brand__mark"></span><span class="brand__name">Brightwave HR</span></div>
    <h2 class="offer-title">Recruitment Special</h2>
    <p class="offer-tagline">People are your best asset, right?<br>...No, the right people are!!!!</p>
    <p class="intro">We operate as a HR Business Partner who can benefit<br>your business by providing a cost effective alternative<br>to carrying out your HR function or provide an extension<br>to your existing HR function where needed.</p>
    <ul class="service-list">
      <li>Building HR Information Systems</li>
      <li>HR Administrative Support – PD’s, contracts,<br>templates, policies &amp; procedures &amp; more;</li>
      <li>Strategic HRM/Workforce Planning</li>
      <li>Recruitment &amp; Selection</li>
      <li>Staff On Boarding / Inductions</li>
      <li>Retaining &amp; Engaging employees</li>
      <li>Timely employee/industrial relations advice</li>
      <li>Talent/Succession Planning</li>
      <li>Managing performance / performance management systems</li>
      <li>Assessing and improving organisational and individual capability</li>
      <li>Training and Development Courses &amp; other creative interventions</li>
      <li>Talent Management &amp; Succession Planning</li>
      <li>Workplace Health &amp; Safety compliance</li>
      <li>Exit and Terminations / Outplacement &amp; Career Transition Support</li>
    </ul>
  </section>
</main>
</body>
</html>
```